Refresh web site from year 2003

Voltaro Forma has a web site (https://vfprosjekt.no/) from early 2000 that needs to be refreshed.

Attached are company logo, favicon files, a licensed image to be used, an animation that illustrate the use of one of the products.

Target Market(s)

Industrial customers

Industry/Entity Type

Electrical Switch Board Builders, Automation Industry

Coding

Coded - Design and coding required

Number of Pages Required

3 page

Requirements
Must have
• WordPress site. Use attached animation in the front page (source file is in Adobe Animation format, if adjustments are needed). Product page for two products, "QRT" and "KV-7 Typ B".
Nice to have
• The site should focus on promoting two products QRT and KV-7 Typ B.

```html
<!DOCTYPE html>
<html lang="en">
<head>
<meta charset="utf-8">
<title>Voltaro Forma</title>
<link href="https://fonts.googleapis.com/css2?family=Roboto:wght@400;500;700&family=Kaushan+Script&display=swap" rel="stylesheet">
<style>
:root{
  --navy:#0c3a6e;
  --navy-dark:#0a2f5a;
  --grey:#8f9496;
  --light:#f0f1f4;
  --text:#444b52;
  --muted:#8a9096;
  --white:#fff;
  --line:#e2e5e9;
}
*{box-sizing:border-box;margin:0;padding:0}
html,body{width:1200px;height:3950px;overflow:hidden}
body{font-family:"Roboto",sans-serif;color:var(--text);background:var(--white);position:relative}
.script{font-family:"Kaushan Script",cursive;color:var(--navy);font-weight:400}
a{color:inherit;text-decoration:none}

/* top bar */
.topbar{height:34px;display:flex;font-size:13px;color:var(--white)}
.topbar-social{width:277px;background:#a5a9ad;display:flex;align-items:center;gap:8px;padding-left:111px}
.dot{width:18px;height:18px;border-radius:50%;background:#5e6469;display:inline-block}
.topbar-info{flex:1;background:var(--navy);display:flex;align-items:center;justify-content:flex-end;gap:44px;padding-right:110px}
.flag{display:inline-block;width:14px;height:14px;border-radius:50%;background:#c8102e;border:3px solid #1b3f8b;vertical-align:-2px;margin:0 4px}

/* nav */
.nav{height:82px;display:flex;align-items:center;padding:0 110px 0 111px;border-bottom:1px solid var(--line)}
.brand{font-weight:700;font-size:24px;color:var(--navy);display:flex;align-items:center;gap:8px}
.brand-mark{width:14px;height:14px;border-radius:50%;background:var(--navy)}
.menu{margin-left:auto;display:flex;gap:31px;font-size:15px;font-weight:500;color:#1d2329}
.menu .active{color:var(--navy)}
.search{margin-left:30px}

/* hero */
.hero{position:relative;height:602px;overflow:hidden}
.hero-photo{position:absolute;inset:0;background:linear-gradient(90deg,#e9ebee 0%,#dfe3e6 38%,#c8ced2 52%,#9aa39f 70%,#b7bdb9 100%)}
.hero-copy{position:absolute;left:129px;top:200px;width:380px}
.hero-copy h1{font-size:54px;line-height:1.1;margin-bottom:18px}
.hero-copy p{font-size:17px;line-height:28px;color:#1d2329;font-weight:500}
.btn{display:inline-flex;align-items:center;gap:9px;background:var(--navy);color:var(--white);font-weight:700;font-size:15px;border-radius:26px;padding:0 30px;height:48px}
.btn-ic{width:15px;height:15px;border-radius:50%;background:var(--white);position:relative}
.btn-ic:after{content:"";position:absolute;left:4px;top:4px;border:4px solid transparent;border-left:5px solid var(--navy);border-right:0}
.hero .btn{margin-top:28px}

/* section title */
.title{text-align:center;font-size:50px;line-height:1.2}

/* services */
.services{height:662px;padding-top:68px}
.services .lead{width:720px;margin:22px auto 0;text-align:center;font-size:14px;line-height:26px}
.circles{position:relative;height:350px;margin-top:56px}
.circle{position:absolute;top:0;width:350px;height:350px;border-radius:50%;background:var(--navy);color:var(--white);text-align:center;padding:36px 60px 0}
.circle.c1{left:110px}
.circle.c2{left:425px;background:var(--grey);z-index:2}
.circle.c3{left:740px}
.icon-ring{width:122px;height:122px;border-radius:50%;border:11px solid rgba(255,255,255,.25);margin:0 auto;display:flex;align-items:center;justify-content:center}
.icon-ring span{display:block;width:88px;height:88px;border-radius:50%;background:var(--white)}
.circle h3{font-size:19px;font-weight:700;margin:27px 0 20px}
.circle p{font-size:14px;line-height:25px}
.circle.c2 p{color:#eef0f1}

/* products */
.products{height:477px;background:var(--light);padding-top:40px}
.cards{display:flex;gap:32px;margin:40px 112px 0}
.pcard{flex:1;height:243px;background:var(--white);box-shadow:0 3px 14px rgba(0,0,0,.1);display:flex;padding:20px 16px}
.pimg{width:150px;height:205px;background:radial-gradient(ellipse at 50% 30%,#e9d8d6 0%,#b59b97 35%,#2e2a28 60%,#c9bfa8 85%,#fff 100%);border-radius:6px}
.pbody{margin-left:28px;flex:1}
.pbody h3{font-size:20px;font-weight:500;color:#111;margin-top:4px}
.pbody small{display:block;font-size:12px;color:var(--muted);margin:6px 0 14px}
.feats{list-style:none;display:grid;grid-template-columns:155px 1fr;row-gap:8px;font-size:14px}
.feats li{display:flex;gap:8px;align-items:flex-start}
.feats li.wide{grid-column:1/3}
.tick{flex:none;width:13px;height:13px;border-radius:50%;background:var(--navy);position:relative;margin-top:2px}
.tick:after{content:"";position:absolute;left:4px;top:2px;width:3px;height:6px;border:solid #fff;border-width:0 2px 2px 0;transform:rotate(45deg)}
.pbody .btn{margin-top:28px;height:42px;padding:0 24px;font-size:14px}

/* about */
.about{height:527px;background:var(--navy);position:relative;color:#e8edf4}
.about-img{position:absolute;left:107px;top:60px;width:445px;height:400px;border-radius:44% 56% 48% 52%/50% 40% 60% 50%;background:linear-gradient(120deg,#c9ced2,#8a96a2 55%,#3c5a7e)}
.about-copy{position:absolute;left:633px;top:80px;width:456px}
.about-copy h2{font-size:48px;color:var(--white);line-height:1.1;margin-bottom:20px}
.about-copy p{font-size:14px;line-height:26.5px;text-align:justify;margin-bottom:12px}
.btn-light{background:var(--white);color:var(--navy);height:46px;margin-top:28px;padding:0 26px;width:193px;justify-content:center}
.btn-light .btn-ic{background:var(--navy)}
.btn-light .btn-ic:after{border-left-color:var(--white)}

/* news */
.news{height:631px;padding-top:92px}
.ncards{display:flex;gap:28px;margin:30px 112px 0}
.ncard{flex:1;height:386px;background:var(--white);box-shadow:0 3px 14px rgba(0,0,0,.1);border-radius:8px;padding:8px;text-align:center}
.nimg{height:202px;border-radius:6px}
.n1{background:linear-gradient(90deg,#6c7a82,#d6dadb 45%,#8c979b)}
.n2{background:linear-gradient(90deg,#a8b4bc,#4f6170 50%,#c4ccd1)}
.n3{background:linear-gradient(90deg,#c8cdd0,#e8eaeb 50%,#b0b6b9)}
.ndate{font-size:13px;color:#5d646b;margin-top:26px}
.ndate:before{content:"";display:inline-block;width:11px;height:11px;border:1.5px solid #8a9096;border-radius:2px;margin-right:7px;vertical-align:-1px}
.ncard h3{font-size:16px;font-weight:700;color:#111;margin:10px 0 12px}
.ncard p{font-size:14px;line-height:22px;color:#6c737a;padding:0 16px}
.more{display:inline-flex;align-items:center;gap:7px;margin-top:18px;font-weight:700;font-size:15px;color:var(--navy)}
.more .btn-ic{background:var(--navy)}
.more .btn-ic:after{border-left-color:var(--white)}

/* contact */
.contact{height:578px;background:var(--light);padding-top:50px}
.form{width:896px;margin:38px auto 0;display:grid;grid-template-columns:1fr 1fr;gap:26px 26px}
.field{height:49px;background:var(--white);border:1px solid #e4e6ea;font-size:13px;color:#8a9096;display:flex;align-items:center;padding-left:18px;gap:7px}
.field.msg{grid-column:1/3;height:110px;align-items:flex-start;padding-top:16px}
.field i{width:9px;height:9px;border:1.5px solid #9aa0a6;border-radius:50%;display:inline-block}
.submit{text-align:center;margin-top:44px}
.submit .btn{width:210px;justify-content:center}

/* footer */
.footer{height:357px;background:var(--navy);color:var(--white);position:relative}
.f-brand{position:absolute;left:114px;top:90px;font-size:40px;font-weight:700;width:230px;line-height:1.1}
.f-social{position:absolute;left:142px;top:213px;display:flex;gap:8px}
.f-social span{width:36px;height:36px;border-radius:50%;background:var(--white)}
.fcol{position:absolute;top:68px}
.fcol h4{font-size:18px;font-weight:700;margin-bottom:18px}
.fcol ul{list-style:none;font-size:14px}
.fcol li{margin-bottom:17px}
.fcol li.arr:before{content:"\203A\203A";margin-right:10px;font-size:13px}
.c-links{left:444px}
.c-imp{left:650px}
.c-contact{left:863px}
.c-contact li{display:flex;gap:16px;line-height:22px;margin-bottom:11px}
.c-contact li svg{flex:none;margin-top:4px}
.copy{position:absolute;left:0;right:0;bottom:16px;text-align:center;font-size:13px}
.chat{position:absolute;right:34px;bottom:54px;width:38px;height:38px;border-radius:50%;background:var(--white)}
</style>
</head>
<body>

<header>
  <div class="topbar">
    <div class="topbar-social"><span class="dot"></span><span class="dot"></span><span class="dot"></span></div>
    <div class="topbar-info">
      <span>&#9742; 922 47 310</span>
      <span>&#9993; post@vfprosjekt.no</span>
      <span>Select language: <span class="flag"></span>Eng &#9662;</span>
    </div>
  </div>
  <nav class="nav">
    <a class="brand" href="#"><span class="brand-mark"></span>Voltaro Forma</a>
    <div class="menu">
      <a class="active" href="#">Home</a><a href="#">Services</a><a href="#">Products</a><a href="#">About us</a><a href="#">Pressure calculator</a><a href="#">News</a><a href="#">Contact</a>
    </div>
    <svg class="search" width="14" height="14" viewBox="0 0 14 14"><circle cx="6" cy="6" r="4.5" fill="none" stroke="#1d2329" stroke-width="2"/><line x1="9.5" y1="9.5" x2="13" y2="13" stroke="#1d2329" stroke-width="2"/></svg>
  </nav>
</header>

<section class="hero">
  <div class="hero-photo" role="img" aria-label="Photo of industrial electrical switchboard cabinets with indicator lamps"></div>
  <div class="hero-copy">
    <h1 class="script">Voltaro Forma</h1>
    <p>Voltaro Forma is a production and development company for electronics with an emphasis</p>
    <a class="btn" href="#">GET STARTED <span class="btn-ic"></span></a>
  </div>
</section>

<section class="services">
  <h2 class="title script">Our Services</h2>
  <p class="lead">Our business idea is to contribute with good and cost-effective electronics products for the industrial market, as well as seek and further develop solutions for new and existing concepts.</p>
  <div class="circles">
    <div class="circle c1"><div class="icon-ring"><span></span></div><h3>Production</h3><p>Small series production of electronics units in the number of 10 to 200 units.</p></div>
    <div class="circle c2"><div class="icon-ring"><span></span></div><h3>Development</h3><p>Development of product idea for finished product in collaboration with customer.</p></div>
    <div class="circle c3"><div class="icon-ring"><span></span></div><h3>Design</h3><p>Designing of electronics and printed circuit boards for pre-assembled and tested unit.</p></div>
  </div>
</section>

<section class="products">
  <h2 class="title script">Our Products</h2>
  <div class="cards">
    <article class="pcard">
      <div class="pimg" role="img" aria-label="Product photo of the Signal indicator lamp"></div>
      <div class="pbody">
        <h3>Signal</h3>
        <small>lamps with built-in LED bulb</small>
        <ul class="feats">
          <li><span class="tick"></span>Easy installation</li><li><span class="tick"></span>Low cost</li>
          <li><span class="tick"></span>Good view</li><li><span class="tick"></span>Long life</li>
          <li class="wide"><span class="tick"></span>At an angle</li>
        </ul>
        <a class="btn" href="#">LEARN MORE <span class="btn-ic"></span></a>
      </div>
    </article>
    <article class="pcard">
      <div class="pimg" role="img" aria-label="Product photo of the Switch position indicator"></div>
      <div class="pbody">
        <h3>Switch position</h3>
        <small>indicators Indicators with light row (LED design)</small>
        <ul class="feats">
          <li><span class="tick"></span>Easy installation</li><li><span class="tick"></span>At an angle</li>
          <li><span class="tick"></span>Good view</li><li><span class="tick"></span>Low cost</li>
          <li class="wide"><span class="tick"></span>Save space and installation: Combine two lamps in one.</li>
        </ul>
        <a class="btn" href="#" style="margin-top:18px">LEARN MORE <span class="btn-ic"></span></a>
      </div>
    </article>
  </div>
</section>

<section class="about">
  <div class="about-img" role="img" aria-label="Switchboard cabinets seen through a curved shape"></div>
  <div class="about-copy">
    <h2 class="script">About us</h2>
    <p>Voltaro Forma is a production and development company for electronics with an emphasis on small series production. We are currently 2 employees with good and relevant access to extra expertise in the established network. The company was established in 1985 and has since 2001 taken over production equipment and production basis from another company in the same industry.</p>
    <p>Norvek Elektronikk A / S 's production department for electronics was closed down and sold in July 2001 .</p>
    <a class="btn btn-light" href="#">LEARN MORE <span class="btn-ic"></span></a>
  </div>
</section>

<section class="news">
  <h2 class="title script">Latest News</h2>
  <div class="ncards">
    <article class="ncard"><div class="nimg n1" role="img" aria-label="Photo of switchboard cabinets"></div><div class="ndate">January 30, 2022</div><h3>Lorem ipsum dolor sit amet</h3><p>Sed ut perspiciatis unde omnis iste natus error sit voluptatem accusantium</p><a class="more" href="#">READ MORE <span class="btn-ic"></span></a></article>
    <article class="ncard"><div class="nimg n2" role="img" aria-label="Photo of a control panel with meters"></div><div class="ndate">January 30, 2022</div><h3>Lorem ipsum dolor sit amet</h3><p>Sed ut perspiciatis unde omnis iste natus error sit voluptatem accusantium</p><a class="more" href="#">READ MORE <span class="btn-ic"></span></a></article>
    <article class="ncard"><div class="nimg n3" role="img" aria-label="Photo of a switchgear unit"></div><div class="ndate">January 30, 2022</div><h3>Lorem ipsum dolor sit amet</h3><p>Sed ut perspiciatis unde omnis iste natus error sit voluptatem accusantium</p><a class="more" href="#">READ MORE <span class="btn-ic"></span></a></article>
  </div>
</section>

<section class="contact">
  <h2 class="title script">Contact Us</h2>
  <div class="form">
    <div class="field"><i></i>First Name</div>
    <div class="field"><i></i>First Name</div>
    <div class="field"><i></i>Email Address</div>
    <div class="field"><i></i>Phone number</div>
    <div class="field msg"><i></i>Message</div>
  </div>
  <div class="submit"><a class="btn" href="#">SUBMIT NOW <span class="btn-ic"></span></a></div>
</section>

<footer class="footer">
  <div class="f-brand">Voltaro Forma</div>
  <div class="f-social"><span></span><span></span><span></span><span></span></div>
  <div class="fcol c-links"><h4>Quick Links</h4><ul><li class="arr">Home</li><li class="arr">Services</li><li class="arr">Products</li><li class="arr">About us</li><li class="arr">Contact</li></ul></div>
  <div class="fcol c-imp"><h4>Important</h4><ul><li class="arr">Terms of Use</li><li class="arr">Site Map</li><li class="arr">Privacy Policy</li><li class="arr">Disclaimer</li></ul></div>
  <div class="fcol c-contact"><h4>Contact us</h4><ul>
    <li><svg width="12" height="14" viewBox="0 0 12 14"><path d="M6 0a5 5 0 0 1 5 5c0 4-5 9-5 9S1 9 1 5a5 5 0 0 1 5-5z" fill="#fff"/><circle cx="6" cy="5" r="2" fill="#0c3a6e"/></svg><span>Lindeveien 48 4630<br>Kristiansand Norway</span></li>
    <li><svg width="12" height="14" viewBox="0 0 12 14"><rect x="1" y="0" width="10" height="14" rx="2" fill="#fff"/></svg><span>922 47 310</span></li>
    <li><svg width="12" height="14" viewBox="0 0 12 14"><rect x="0" y="4" width="12" height="9" fill="#fff"/><rect x="3" y="0" width="6" height="4" fill="#fff"/></svg><span>+ 47 381 00 214</span></li>
    <li><svg width="12" height="14" viewBox="0 0 12 14"><rect x=".5" y="3" width="11" height="8" fill="none" stroke="#fff"/><path d="M.5 3l5.5 4 5.5-4" fill="none" stroke="#fff"/></svg><span>post@vfprosjekt.no</span></li>
  </ul></div>
  <div class="chat"></div>
  <div class="copy">© 2022 Voltaro Forma | All Rights Reserved</div>
</footer>

</body>
</html>
```